Personalised Poetry business needs a business card designed

I am a writer that specialises in personalised poetry for people for significant life events.
I want a business card that stands out and portrays class and professionalism but is also welcoming & indicates warmth and honesty.
I'm happy with the logo that was designed for me, I would like to see it in raised print on the business card. I am open to suggestions on colours but think perhaps gold or silver writing for the logo would look good. I would like just the logo and my name and contact details on the front of the card. On the back of the card, I would like a list of the different events I provide poems for I will upload a photo of my current business card for reference. My current logo has a shading behind it that I don't like, I just want the words of the logo without any background colour

Target Market(s)

People wanting to provide a unique gift to someone special in their life

Industry/Entity Type

Writer

Contact Information for Business Card

Logo, my name and contact details on the front and a list of all the events I write poetry for on the back

Font styles to use
Script

Requirements
Must have
• I would like to see the logo, if possible, in a raised type of print on the card so that you can feel the actual words. I would like to have a glossy finish to the card and be able to print it on good quality board
Should not have
• The shading that is currently behind the logo on my current business card

```html
<!DOCTYPE html>
<html lang="en">
<head>
<meta charset="utf-8">
<title>Lines for Always – Business Card</title>
<link rel="stylesheet" href="https://fonts.googleapis.com/css2?family=Allura&family=Quicksand:wght@400;600&display=swap">
<style>
  :root {
    --page: #e4e5e8;
    --card-dark: #38383a;
    --gold: #d9ae3c;
    --ink: #2a2620;
  }
  * { box-sizing: border-box; margin: 0; padding: 0; }
  html, body {
    width: 1200px; height: 800px; overflow: hidden;
    background: var(--page);
  }
  .canvas {
    position: relative; width: 1200px; height: 800px;
    display: flex; align-items: center; justify-content: center; gap: 40px;
  }
  .card {
    position: relative; width: 520px; height: 300px;
    background: var(--card-dark);
    border-radius: 4px; overflow: hidden;
    box-shadow: 0 10px 28px rgba(0,0,0,0.18);
    font-family: "Quicksand", sans-serif;
  }
  .card-wave { position: absolute; inset: 0; width: 100%; height: 100%; }
  .brand-name {
    position: absolute; left: 34px; top: 28px;
    font-family: "Quicksand", sans-serif;
    font-size: 34px; font-weight: 400; line-height: 1;
    color: var(--gold);
  }
  .brand-tagline {
    position: absolute; left: 120px; top: 76px;
    font-size: 16px; color: var(--gold); letter-spacing: 0.3px;
  }
  .owner-name {
    position: absolute; right: 96px; top: 174px;
    font-family: "Allura", cursive;
    font-size: 36px; line-height: 1; color: var(--ink);
  }
  .contact-list {
    position: absolute; right: 92px; top: 222px;
    list-style: none; text-align: right;
    font-size: 13px; color: var(--ink); line-height: 1.55;
  }
  .contact-list li { display: flex; align-items: center; justify-content: flex-end; gap: 6px; }
  .contact-icon { width: 11px; height: 11px; }
  .services-headline {
    position: absolute; right: 96px; top: 180px;
    text-align: right; font-weight: 600;
    font-size: 17px; line-height: 1.3; color: var(--ink);
  }
  .services-list {
    position: absolute; left: 28px; top: 246px;
    list-style: none; font-size: 11.5px; line-height: 1.6; color: var(--ink);
  }
</style>
</head>
<body>
<main class="canvas">

  <section class="card card-front" aria-label="Business card front">
    <svg class="card-wave" viewBox="0 0 520 300" aria-hidden="true">
      <defs>
        <linearGradient id="goldFront" x1="0" y1="0" x2="1" y2="0.4">
          <stop offset="0" stop-color="#b07a1c"/>
          <stop offset="0.3" stop-color="#f6d66a"/>
          <stop offset="0.55" stop-color="#e6b83a"/>
          <stop offset="0.8" stop-color="#a8701a"/>
          <stop offset="1" stop-color="#f2cf5e"/>
        </linearGradient>
      </defs>
      <path d="M0,140 C100,130 160,150 220,160 C300,172 330,140 390,140 C470,140 480,230 460,300 L0,300 Z" fill="url(#goldFront)"/>
      <path d="M0,132 C100,122 160,142 220,152 C300,164 330,131 392,131 C482,131 492,230 472,300" fill="none" stroke="url(#goldFront)" stroke-width="2"/>
    </svg>
    <div class="brand-name">Lines for Always</div>
    <div class="brand-tagline">Personalised Poetry</div>
    <div class="owner-name">Marcus Ellery</div>
    <ul class="contact-list">
      <li>0400 555 017
        <svg class="contact-icon" viewBox="0 0 12 12" aria-hidden="true"><rect x="3" y="0.8" width="6" height="10.4" rx="1" fill="none" stroke="#2a2620" stroke-width="1.1"/><line x1="5" y1="9.4" x2="7" y2="9.4" stroke="#2a2620" stroke-width="1"/></svg>
      </li>
      <li>marcus@linesforalways.com
        <svg class="contact-icon" viewBox="0 0 12 12" aria-hidden="true"><rect x="0.8" y="2.5" width="10.4" height="7" fill="#2a2620"/><path d="M1,3 L6,7 L11,3" fill="none" stroke="#e6b83a" stroke-width="0.9"/></svg>
      </li>
    </ul>
  </section>

  <section class="card card-back" aria-label="Business card back">
    <svg class="card-wave" viewBox="0 0 520 300" aria-hidden="true">
      <defs>
        <linearGradient id="goldBack" x1="0" y1="0" x2="1" y2="0.4">
          <stop offset="0" stop-color="#b07a1c"/>
          <stop offset="0.3" stop-color="#f6d66a"/>
          <stop offset="0.55" stop-color="#e6b83a"/>
          <stop offset="0.8" stop-color="#a8701a"/>
          <stop offset="1" stop-color="#f2cf5e"/>
        </linearGradient>
      </defs>
      <path d="M0,140 C100,130 160,150 220,160 C300,172 330,140 390,140 C470,140 480,230 460,300 L0,300 Z" fill="url(#goldBack)"/>
      <path d="M0,132 C100,122 160,142 220,152 C300,164 330,131 392,131 C482,131 492,230 472,300" fill="none" stroke="url(#goldBack)" stroke-width="2"/>
    </svg>
    <div class="brand-name">Lines for Always</div>
    <div class="brand-tagline">Personalised Poetry</div>
    <h2 class="services-headline">Momentous Life Events<br>Personalised in Poetry</h2>
    <ul class="services-list">
      <li>Wedding &amp; Anniversaries / Birthday &amp; Christmas / Valentines Day</li>
      <li>Retirements, Business &amp; Corporate Events / Funerals &amp; Eulogies</li>
    </ul>
  </section>

</main>
</body>
</html>
```